HORIZON - and teamwork crafts of today

I´m writing a book about CHANGE and the skills leaders needs to embody the transformation from being amanager to become leaders.
The title of the book in Icelandic is the same as the name of the project (which I want to be used on the designes is:) SKÝJAFAR
(with the subtitle:) og hugrekkislist samtímans

Change is not controlled or managed – Leading effective change is an art form which is one of the big reasons for why 70% of changes within companies fail. The main reason however, is that managers are tasked with managing and directing them. The art form of change is to put it in the hands of leaders who possess the emotional intelligence that is needed – all their other advantages intact – to lead change all the way.

The big problem when it comes to change is that there are too many managers and too few leaders within companies – leaders who possess emotional intelligence which is the most important skill a leader embodies to empower change. A leader has what it takes to empower followership.

A manager tends to push and control, make decisions that he presupposes others to implement the way he expects. An emotionally competent leader leads by example and enhances followership on that journey because of the trust and respect he has earned.

In few words: SOFT SKILLS ARE THE NEW HARD SKILLS!

```html
<!DOCTYPE html>
<html lang="is">
<head>
<meta charset="utf-8">
<title>SKÝJAFAR – og hugrekkislist samtímans</title>
<link rel="stylesheet" href="https://fonts.googleapis.com/css2?family=Oswald:wght@500&family=Source+Sans+3:wght@600;700&display=swap">
<style>
  :root {
    --paper: #f1f2f6;
    --paper-shade: #d9dadf;
    --paper-deep: #b9babf;
    --hole-red: #e3130d;
    --hole-red-deep: #b80a06;
    --title-white: #ffffff;
    --ink: #2f2f3c;
    --author-ink: #3a3a4c;
  }
  html, body {
    margin: 0;
    padding: 0;
    width: 1200px;
    height: 1200px;
    overflow: hidden;
    background: var(--paper);
  }
  .book-cover {
    position: relative;
    width: 1200px;
    height: 1200px;
    background: var(--paper);
    overflow: hidden;
  }
  .subtitle {
    position: absolute;
    top: 58px;
    left: 0;
    width: 100%;
    margin: 0;
    text-align: center;
    font-family: "Source Sans 3", sans-serif;
    font-weight: 700;
    font-size: 25px;
    letter-spacing: 2.2px;
    color: var(--ink);
    text-transform: uppercase;
  }
  .torn-hole {
    position: absolute;
    left: 120px;
    top: 130px;
    width: 950px;
    height: 950px;
    border-radius: 50%;
    background: radial-gradient(circle at 50% 50%,
      var(--hole-red) 0%,
      var(--hole-red) 34%,
      var(--hole-red-deep) 42%,
      var(--paper-deep) 44%,
      var(--paper-shade) 49%,
      var(--paper) 58%);
  }
  .title {
    position: absolute;
    top: 488px;
    left: 0;
    width: 1190px;
    margin: 0;
    text-align: center;
    font-family: "Oswald", sans-serif;
    font-weight: 500;
    font-size: 218px;
    line-height: 1;
    letter-spacing: 2px;
    color: var(--title-white);
  }
  .author {
    position: absolute;
    top: 1098px;
    left: 0;
    width: 100%;
    margin: 0;
    text-align: center;
    font-family: "Source Sans 3", sans-serif;
    font-weight: 700;
    font-size: 54px;
    letter-spacing: 4px;
    color: var(--author-ink);
  }
</style>
</head>
<body>
  <main class="book-cover">
    <p class="subtitle">og hugrekkislist samtímans</p>
    <div class="torn-hole" role="img" aria-label="White paper torn open in a round hole revealing bright red paper beneath"></div>
    <h1 class="title">SKÝJAFAR</h1>
    <p class="author">AUTHOR NAME</p>
  </main>
</body>
</html>
```